Plumbing Company After Business Card

Business card for a plumbing business that offers a variety of plumbing services including maintenance, domestic and commercial plumbing. My main focus is to offer high quality professional service. A logo on the card would be ideal. Any other questions feel free to email. Cheers

Looking for something modern and upmarket with preferably a matte black background

Business name is Crestline Plumbing and Gas

Industry/Entity Type

Plumbing

Contact Information for Business Card

Crestline Plumbing and Gas
Marcus Thorvale
0472519306
14 Karrabee Drive, Larkvale 3561
crestlineplumbing@mailbay.com.au
ABN 64 915 207 338

Font styles to use
Sans Serif

Colors
1b1b1b
ffffff
3377b5

Requirements
Must have
• Domestic
• Commercial
• Maintenance

```html
<!DOCTYPE html>
<html lang="en">
<head>
<meta charset="utf-8">
<title>Crestline Plumbing and Gas – Business Card</title>
<link href="https://fonts.googleapis.com/css2?family=Saira:ital,wght@0,400;0,700;1,400&display=swap" rel="stylesheet">
<style>
  :root {
    --page-bg: #b7afad;
    --card-black: #030303;
    --card-warm: #4a3f3b;
    --card-mid: #1b1b1b;
    --accent-blue: #1b9bd7;
    --text-white: #ffffff;
  }
  * { box-sizing: border-box; margin: 0; padding: 0; }
  html, body {
    width: 1200px; height: 1200px; overflow: hidden;
    background: var(--page-bg);
    font-family: "Saira", sans-serif;
    color: var(--text-white);
  }
  .sheet {
    width: 1200px; height: 1200px;
    display: flex; align-items: center; justify-content: center; gap: 40px;
  }
  .card {
    position: relative;
    width: 540px; height: 310px;
    background: var(--card-black);
    overflow: hidden;
    box-shadow: 0 6px 14px rgba(0,0,0,0.25);
  }

  /* Front */
  .card--front {
    background: radial-gradient(ellipse at 50% 40%, var(--card-warm) 0%, var(--card-mid) 45%, var(--card-black) 80%);
  }
  .wordmark {
    font-weight: 700;
    color: var(--accent-blue);
    text-transform: uppercase;
    line-height: 1;
    letter-spacing: 0.02em;
  }
  .card--front .wordmark {
    position: absolute; left: 0; right: 0; top: 100px;
    text-align: center; font-size: 34px;
  }
  .wordmark span { display: block; }
  .wordmark .wordmark__sub { font-size: 0.62em; margin-top: 6px; }
  .service-strip {
    position: absolute; left: 0; right: 0; bottom: 18px; height: 34px;
    background: var(--card-black);
    display: flex; justify-content: space-around; align-items: center;
    list-style: none;
    font-size: 16px; font-style: italic;
  }
  .service { display: flex; align-items: center; gap: 6px; }
  .service svg { width: 14px; height: 14px; }

  /* Back */
  .card--back .panel { position: absolute; inset: 0; }
  .card--back .wordmark {
    position: absolute; left: 28px; top: 30px; font-size: 24px;
  }
  .contact-name {
    position: absolute; right: 26px; top: 56px;
    font-size: 22px; font-weight: 700; text-align: right; line-height: 1.1;
  }
  .contact-name .first { color: var(--accent-blue); }
  .contact-phone {
    position: absolute; right: 26px; top: 86px;
    font-size: 16px; display: flex; align-items: center; gap: 6px;
  }
  .contact-details {
    position: absolute; right: 26px; bottom: 22px;
    text-align: right; font-size: 16px; line-height: 1.25; font-style: normal;
  }
  .contact-details .row { display: flex; justify-content: flex-end; align-items: center; gap: 6px; }
  .icon { width: 14px; height: 14px; flex: none; }
</style>
</head>
<body>
<main class="sheet">

  <section class="card card--front" aria-label="Card front">
    <div class="wordmark">
      <span>Crestline Plumbing</span>
      <span class="wordmark__sub">and Gas</span>
    </div>
    <ul class="service-strip">
      <li class="service">
        <svg viewBox="0 0 14 14"><path d="M2 8 L6 12 L12 2" fill="none" stroke="var(--accent-blue)" stroke-width="2"/></svg>
        Domestic
      </li>
      <li class="service">
        <svg viewBox="0 0 14 14"><path d="M2 8 L6 12 L12 2" fill="none" stroke="var(--accent-blue)" stroke-width="2"/></svg>
        Commercial
      </li>
      <li class="service">
        <svg viewBox="0 0 14 14"><path d="M2 8 L6 12 L12 2" fill="none" stroke="var(--accent-blue)" stroke-width="2"/></svg>
        Maintenance
      </li>
    </ul>
  </section>

  <section class="card card--back" aria-label="Card back">
    <svg class="panel" viewBox="0 0 540 310" preserveAspectRatio="none">
      <defs>
        <radialGradient id="panelGlow" cx="0.15" cy="0.55" r="0.6">
          <stop offset="0" stop-color="#4a3f3b"/>
          <stop offset="0.6" stop-color="#1b1b1b"/>
          <stop offset="1" stop-color="#080808"/>
        </radialGradient>
      </defs>
      <rect width="540" height="310" fill="var(--card-black)"/>
      <polygon points="0,0 330,0 90,310 0,310" fill="url(#panelGlow)"/>
    </svg>

    <div class="wordmark">
      <span>Crestline Plumbing</span>
      <span class="wordmark__sub">and Gas</span>
    </div>

    <h2 class="contact-name"><span class="first">Marcus</span>Thorvale</h2>
    <p class="contact-phone">
      <svg class="icon" viewBox="0 0 14 14"><circle cx="7" cy="7" r="6" fill="none" stroke="var(--accent-blue)" stroke-width="1.4"/><path d="M5 4 Q4 7 7 10 L8.5 9 L7.5 7.5 L6.5 8 Q5.5 6.5 6 5.5 L6.5 5 Z" fill="var(--accent-blue)"/></svg>
      0472519306
    </p>

    <address class="contact-details">
      <div class="row">
        <svg class="icon" viewBox="0 0 14 14"><path d="M7 1 A4.5 4.5 0 0 1 11.5 5.5 C11.5 8.5 7 13 7 13 C7 13 2.5 8.5 2.5 5.5 A4.5 4.5 0 0 1 7 1 Z" fill="var(--accent-blue)"/><circle cx="7" cy="5.5" r="1.6" fill="var(--card-black)"/></svg>
        14 Karrabee Drive
      </div>
      <div class="row">Larkvale 3561</div>
      <div class="row">
        <svg class="icon" viewBox="0 0 14 14"><rect x="1" y="3" width="12" height="8" fill="none" stroke="var(--accent-blue)" stroke-width="1.4"/><path d="M1 3 L7 8 L13 3" fill="none" stroke="var(--accent-blue)" stroke-width="1.4"/></svg>
        crestlineplumbing@mailbay.com.au
      </div>
      <div class="row">ABN 64 915 207 338</div>
    </address>
  </section>

</main>
</body>
</html>
```